Forest Consultant/Timber Buyer needs a clean business card

We are a forestry consulting and timber buying company. We meet with private landowners and assist them with timber management and timber harvesting. We would like a professional business card, please no clip art. logo is blue and white but would like to see a gray,silver, or some other color incorporated. Would like basic contact info. Would like to the layout to be creative and sleek but masculine.

Target Market(s)

private landowners

Industry/Entity Type

Business

Contact Information for Business Card

name,position, cell number, office number, email, website. This might be to cluttered. Basic contact info is what we are looking for.

Contact info can all be on one side with logo on the other.

Font styles to use
Serif
Sans Serif

Colors
0255a3
ffffff
aaaaaa

Requirements
Must have
• We just want it professional.
Nice to have
• Creative layout.
Should not have
• please no clip art of log trucks etc.

```html
<!DOCTYPE html>
<html lang="en">
<head>
<meta charset="utf-8">
<title>Ridgeline Land &amp; Timber – Business Card</title>
<link rel="stylesheet" href="https://fonts.googleapis.com/css2?family=Open+Sans:wght@400;600;700&display=swap">
<style>
  :root {
    --brand-blue: #0255a3;
    --bright-blue: #1a8fd6;
    --deep-blue: #0a4f96;
    --charcoal: #2a2c2e;
    --charcoal-light: #4a4d50;
    --silver: #aaaaaa;
    --white: #ffffff;
    --name-accent: #8a4a1c;
    --backdrop: #e8e6e3;
  }
  * { margin: 0; padding: 0; box-sizing: border-box; }
  html, body {
    width: 1200px; height: 800px; overflow: hidden;
    background: var(--backdrop);
    font-family: "Open Sans", Arial, sans-serif;
  }
  .canvas { position: relative; width: 1200px; height: 800px; }

  /* Front card – logo side */
  .card-front {
    position: absolute; left: 130px; top: 150px;
    width: 300px; height: 520px;
    background: linear-gradient(160deg, var(--bright-blue) 0%, var(--brand-blue) 60%, var(--deep-blue) 100%);
    box-shadow: 0 10px 30px rgba(0,0,0,.25);
    overflow: hidden;
  }
  .card-front .forest-fill {
    position: absolute; left: 70px; top: 20px; width: 230px; height: 160px;
    background: linear-gradient(180deg, rgba(10,60,120,.0) 0%, rgba(10,60,120,.45) 70%, rgba(10,60,120,.0) 100%);
  }
  .front-brand {
    position: absolute; left: 150px; top: 270px;
    transform: rotate(90deg); transform-origin: left top;
    color: var(--white); white-space: nowrap;
  }
  .front-brand .brand-name { font-size: 40px; font-weight: 600; letter-spacing: 2px; line-height: 1; }
  .front-brand .brand-tag { font-size: 13px; font-weight: 600; letter-spacing: 7px; margin-top: 6px; padding-left: 14px; }

  /* Back card – contact side */
  .card-back {
    position: absolute; left: 490px; top: 210px;
    width: 620px; height: 360px;
    background: linear-gradient(200deg, var(--charcoal-light) 0%, var(--charcoal) 55%, #1c1d1f 100%);
    box-shadow: 0 10px 30px rgba(0,0,0,.3);
    overflow: hidden;
  }
  .card-back svg.band { position: absolute; inset: 0; }
  .card-back .forest-fill {
    position: absolute; right: 0; top: 120px; width: 200px; height: 150px;
    background: linear-gradient(90deg, rgba(120,120,120,0) 0%, rgba(110,110,110,.7) 50%, rgba(90,90,90,.5) 100%);
  }
  .back-brand {
    position: absolute; left: 300px; top: 28px;
    display: flex; align-items: center; gap: 12px;
    color: var(--brand-blue);
  }
  .back-brand .brand-dot { width: 34px; height: 34px; border-radius: 50%; background: var(--brand-blue); }
  .back-brand .brand-name { font-size: 34px; font-weight: 700; letter-spacing: 2px; line-height: 1; }
  .back-brand .brand-tag { font-size: 10px; font-weight: 600; letter-spacing: 5px; color: var(--silver); margin-top: 4px; text-align: right; }

  .contact-lines { position: absolute; left: 26px; top: 132px; color: var(--white); font-size: 13px; }
  .contact-lines li { list-style: none; display: flex; align-items: center; gap: 10px; height: 20px; }
  .contact-lines svg { width: 12px; height: 12px; }

  .person { position: absolute; left: 300px; top: 165px; }
  .person .name { color: var(--name-accent); font-size: 20px; font-weight: 600; letter-spacing: .5px; }
  .person .role { color: var(--white); font-size: 11px; font-weight: 600; letter-spacing: .5px; }

  .address { position: absolute; left: 320px; top: 260px; color: var(--white); font-size: 14px; line-height: 1.45; }
  .address .web { margin-top: 4px; }
</style>
</head>
<body>
<main class="canvas">

  <section class="card-front" aria-label="Business card front">
    <div class="forest-fill" role="img" aria-label="Faint silhouette of a pine tree line"></div>
    <div class="front-brand">
      <div class="brand-name">RIDGELINE</div>
      <div class="brand-tag">LAND &amp; TIMBER</div>
    </div>
  </section>

  <section class="card-back" aria-label="Business card back">
    <svg class="band" viewBox="0 0 620 360" width="620" height="360" aria-hidden="true">
      <defs>
        <linearGradient id="blueBand" x1="0" y1="0" x2="1" y2="1">
          <stop offset="0" stop-color="#1a8fd6"/>
          <stop offset="1" stop-color="#0255a3"/>
        </linearGradient>
      </defs>
      <path d="M0,104 Q330,72 620,262 L620,360 L0,360 Z" fill="#8d9094"/>
      <path d="M0,112 Q330,80 620,270 L620,360 L0,360 Z" fill="url(#blueBand)"/>
    </svg>
    <div class="forest-fill" role="img" aria-label="Silhouette of pine trees"></div>

    <div class="back-brand">
      <span class="brand-dot"></span>
      <div>
        <div class="brand-name">RIDGELINE</div>
        <div class="brand-tag">LAND &amp; TIMBER</div>
      </div>
    </div>

    <ul class="contact-lines">
      <li><svg viewBox="0 0 12 12"><rect width="12" height="12" rx="2" fill="#aaaaaa"/><rect x="4" y="2" width="4" height="8" rx="1" fill="#2a2c2e"/></svg>0400 555 210</li>
      <li><svg viewBox="0 0 12 12"><rect width="12" height="12" rx="2" fill="#aaaaaa"/><rect x="2" y="3" width="8" height="6" rx="1" fill="#2a2c2e"/></svg>0400 555 210</li>
      <li><svg viewBox="0 0 12 12"><rect width="12" height="12" rx="2" fill="#aaaaaa"/><path d="M2,3 H10 V9 H2 Z M2,3 L6,6.5 L10,3" fill="none" stroke="#2a2c2e" stroke-width="1"/></svg>amorrow@ridgelinetimber.com.au</li>
    </ul>

    <div class="person">
      <div class="name">ALEX MORROW</div>
      <div class="role">FINANCE MANAGER</div>
    </div>

    <address class="address" style="font-style:normal">
      <div>SUITE 4, 27 BARROW STREET</div>
      <div>PINE HILL, QLD 4090.</div>
      <div class="web">www.ridgelinetimber.com.au</div>
    </address>
  </section>

</main>
</body>
</html>
```